PowerPoint Template Design for business consulting company in Silicon Valley

I need a PowerPoint template to use as the starting point for new presentations. I have a logo but now need design that supports this. I've attached a very descriptive PDF that explains exactly what I need. Here is a list of deliverables: 1. PowerPoint Template that I will use as the starter presentation for all new Vantor Bellway presentationsDesigns for the following slides: See picture below for examples of structure:2. Title slide with subtitle3. Section header4. Title and body5. Title and 2 columns6. Title and 3 columns7. One column text8. Editable timeline to show months, or steps for a process9. Bullet design for unordered list (can be graphic)10. Bullet design for ordered list11. Recommended fonts for each design: Title, subtitle, list, captionOPTIONAL: Possible graphic elements to be used for section title slide backgrounds or graphic elements:--Your team / my team / people on project--Goals for project / presentation--Editable Timeline--Speaking--Writing--Listening--People collaborating / helping each otherI am happy to accept proposals for developing these optional elements in a separate project.

Requirements
Must have
• Must be FLAT design.
• Not flashy or garish. Must be subtle.

```html
<!DOCTYPE html>
<html lang="en">
<head>
<meta charset="utf-8">
<title>Vantor Bellway — Presentation Template Slides</title>
<link href="https://fonts.googleapis.com/css2?family=Montserrat:wght@800&family=Open+Sans:wght@400;600;700&family=Oswald:wght@700&display=swap" rel="stylesheet">
<style>
  :root{
    --blue:#233f98;
    --blue-bright:#1b75c4;
    --green:#1c6f34;
    --grey:#d8d8d8;
    --grey-text:#8a8a8a;
    --ink:#333;
    --pale:#e1eae4;
    --white:#fff;
  }
  *{box-sizing:border-box;margin:0;padding:0}
  html,body{width:1200px;height:1200px;overflow:hidden;background:var(--white)}
  body{position:relative;font-family:"Open Sans",Arial,sans-serif;color:var(--ink)}
  .abs{position:absolute}
  .slide{position:absolute;overflow:hidden;background:var(--white)}
  .title{font-family:"Montserrat",Arial,sans-serif;font-weight:800;color:var(--white);white-space:nowrap;letter-spacing:-.2px}
  .bar{position:absolute;display:flex;align-items:center;padding-left:7px}
  .bar-blue{background:var(--blue)}
  .bar-green{background:var(--green)}
  .photo{position:absolute}
  .brand{font-family:"Open Sans",Arial,sans-serif;font-weight:600;color:var(--green);white-space:nowrap;line-height:1}
  .footer-brand{position:absolute;right:5px;bottom:5px;font-size:5px}
  .tiny{font-size:5.5px;line-height:1.35;color:#666}
  .bullet-list{list-style:none}
  .bullet-list li{height:20px;position:relative}
  .bullet-list li::before{content:"";position:absolute;left:0;top:6px;width:4px;height:4px;border-radius:50%;background:#222}
  .text-box{position:absolute;border:1px solid #ccc;background:var(--white);font-size:11px;padding:4px 6px}
  .text-box p::before{content:"•";margin-right:8px}
  .ph-icon{position:absolute;display:grid;grid-template-columns:repeat(3,7px);gap:2px}
  .ph-icon span{height:6px;background:#c9d3de}
  .ph-icon span:nth-child(2){background:#e3b54a}
  .ph-icon span:nth-child(3){background:#9fc08e}
  .col-head{position:absolute;display:flex;align-items:center;justify-content:center;color:var(--white);font-size:13px}
  .col-body{position:absolute;background:var(--grey);font-size:7px;color:var(--grey-text)}
  .col-body div{height:18px;line-height:18px;padding-left:17px;border-bottom:1px solid #e6e6e6}
  .tl-year{position:absolute;font-weight:700;font-size:10px;width:40px;text-align:center}
  .tl-cap{position:absolute;width:76px;text-align:center;font-size:5px;line-height:1.3;color:#666}
  .vt-year{position:absolute;font-weight:600;font-size:12px;color:#333;width:40px;text-align:right}
  .vt-text{position:absolute;font-size:5.5px;color:#555;line-height:1.9}
  .feature-label{position:absolute;font-size:6px;color:#555;width:175px;line-height:1.4}
  .feature-label b{display:block;font-size:6.5px;color:var(--blue)}
  .option{position:absolute;left:135px;width:239px;height:44px;border:2px solid var(--blue);padding:4px 10px}
  .option h4{font-size:11px;font-weight:600;color:var(--blue);margin-bottom:2px}
  .option p{font-size:4.5px;color:var(--blue);line-height:1.5}
</style>
</head>
<body>

<!-- Title slide -->
<section class="slide" style="left:0;top:0;width:406px;height:233px">
  <div class="photo" role="img" aria-label="Photo of a hand with a pen over a calculator and financial papers" style="inset:0;background:linear-gradient(135deg,#6b6f73 0%,#a9afb4 45%,#d6dadf 70%,#8d9398 100%)"></div>
  <div class="abs" style="left:119px;top:62px;width:170px;height:113px;background:rgba(255,255,255,.78);display:flex;align-items:center;justify-content:center">
    <span class="brand" style="font-size:15px">Vantor Bellway</span>
  </div>
  <div class="abs" style="left:119px;top:175px;width:170px;height:21px;background:rgba(255,255,255,.35);display:flex;align-items:center;justify-content:center">
    <span class="title" style="font-size:11px">CLICK TO ADD TITLE</span>
  </div>
</section>

<!-- Section header -->
<section class="slide" style="left:406px;top:0;width:388px;height:233px">
  <div class="photo" role="img" aria-label="Photo of a business team celebrating with raised arms" style="inset:0;background:linear-gradient(180deg,#3e434b 0%,#5a5f66 45%,#2d3037 100%)"></div>
  <div class="abs" style="left:28px;top:74px;width:94px;height:92px;background:var(--blue)"></div>
  <div class="abs" style="left:28px;top:79px;width:307px;height:88px;border:1px solid rgba(255,255,255,.85);display:flex;align-items:center;padding-left:22px">
    <span class="title" style="font-size:22px">CLICK TO ADD TITLE</span>
  </div>
</section>

<!-- Title and bullets -->
<section class="slide" style="left:794px;top:0;width:406px;height:233px;background:#f8f8f8">
  <div class="bar bar-blue" style="left:0;top:16px;width:378px;height:40px"><span class="title" style="font-size:18px">CLICK TO ADD TITLE</span></div>
  <ul class="bullet-list abs" style="left:25px;top:86px"><li></li><li></li><li></li><li></li><li></li><li></li></ul>
  <span class="brand footer-brand" style="bottom:8px">Vantor Bellway</span>
</section>

<!-- Two columns -->
<section class="slide" style="left:0;top:233px;width:406px;height:227px">
  <div class="bar bar-blue" style="left:0;top:13px;width:380px;height:38px"><span class="title" style="font-size:18px">CLICK TO ADD TITLE</span></div>
  <div class="text-box" style="left:17px;top:64px;width:180px;height:151px"><p>Click to add text</p><div class="ph-icon" style="left:76px;top:80px"><span></span><span></span><span></span><span></span><span></span><span></span></div></div>
  <div class="text-box" style="left:207px;top:64px;width:180px;height:151px"><p>Click to add text</p><div class="ph-icon" style="left:76px;top:80px"><span></span><span></span><span></span><span></span><span></span><span></span></div></div>
  <span class="brand footer-brand" style="bottom:3px">Vantor Bellway</span>
</section>

<!-- Three columns -->
<section class="slide" style="left:406px;top:233px;width:388px;height:227px">
  <div class="bar bar-blue" style="left:2px;top:13px;width:358px;height:38px"><span class="title" style="font-size:18px">CLICK TO ADD TITLE</span></div>
  <div class="col-head" style="left:31px;top:72px;width:97px;height:32px;background:var(--green)">Text here</div>
  <div class="col-body" style="left:31px;top:104px;width:97px;height:87px"><div>Item 01 description</div><div>Item 02 description</div><div>Item 03 description</div><div>Item 04 description</div></div>
  <div class="abs" style="left:31px;top:191px;width:97px;height:8px;background:var(--green)"></div>
  <div class="col-head" style="left:128px;top:57px;width:118px;height:40px;background:var(--blue-bright);font-size:16px">Text here</div>
  <div class="col-body" style="left:128px;top:97px;width:118px;height:112px;padding-top:3px"><div style="height:20px">Item 01 description</div><div style="height:20px">Item 02 description</div><div style="height:20px">Item 03 description</div><div style="height:20px">Item 04 description</div></div>
  <div class="abs" style="left:128px;top:199px;width:118px;height:10px;background:var(--blue-bright)"></div>
  <div class="col-head" style="left:246px;top:72px;width:97px;height:32px;background:var(--green)">Text here</div>
  <div class="col-body" style="left:246px;top:104px;width:97px;height:87px"><div>Item 01 description</div><div>Item 02 description</div><div>Item 03 description</div><div>Item 04 description</div></div>
  <div class="abs" style="left:246px;top:191px;width:97px;height:8px;background:var(--green)"></div>
  <span class="brand footer-brand" style="bottom:6px">Vantor Bellway</span>
</section>

<!-- One column text -->
<section class="slide" style="left:792px;top:233px;width:408px;height:227px">
  <div class="abs" style="left:0;top:0;width:199px;height:220px;background:var(--green)"></div>
  <span class="title abs" style="left:14px;top:11px;font-size:16px">CLICK TO ADD TITLE</span>
  <div class="abs" style="left:24px;top:35px;width:342px;height:170px;background:var(--pale);border:1px solid #c9d4cc;font-size:11px;padding:3px 6px">
    <p>•&nbsp;&nbsp;Click to add text</p>
    <div class="ph-icon" style="left:168px;top:62px"><span></span><span></span><span></span><span></span><span></span><span></span></div>
  </div>
  <span class="brand footer-brand" style="bottom:8px">Vantor Bellway</span>
</section>

<!-- Horizontal timeline -->
<section class="slide" style="left:0;top:465px;width:401px;height:221px">
  <div class="bar bar-green" style="left:0;top:0;width:401px;height:41px"><span class="title" style="font-size:19px">CLICK TO ADD TITLE</span></div>
  <svg class="abs" style="left:0;top:0" width="401" height="221" viewBox="0 0 401 221">
    <line x1="30" y1="123" x2="400" y2="123" stroke="#d0d0d0" stroke-width="1.5"/>
    <g fill="none" stroke-width="3">
      <circle cx="55" cy="121" r="12" stroke="var(--blue)"/><line x1="55" y1="133" x2="55" y2="152" stroke="var(--blue)"/>
      <circle cx="135" cy="121" r="12" stroke="var(--green)"/><line x1="135" y1="109" x2="135" y2="90" stroke="var(--green)"/>
      <circle cx="214" cy="121" r="12" stroke="#e3e3e3"/><line x1="214" y1="133" x2="214" y2="152" stroke="#e3e3e3"/>
      <circle cx="294" cy="121" r="12" stroke="#e3e3e3"/><line x1="294" y1="109" x2="294" y2="90" stroke="#e3e3e3"/>
      <circle cx="373" cy="121" r="12" stroke="var(--blue)"/><line x1="373" y1="133" x2="373" y2="152" stroke="var(--blue)"/>
    </g>
    <g>
      <circle cx="55" cy="154" r="3" fill="var(--blue)"/><circle cx="135" cy="88" r="3" fill="var(--green)"/>
      <circle cx="214" cy="154" r="3" fill="#e3e3e3"/><circle cx="294" cy="88" r="3" fill="#e3e3e3"/>
      <circle cx="373" cy="154" r="3" fill="var(--blue)"/>
    </g>
  </svg>
  <div class="tl-year" style="left:35px;top:87px;color:var(--blue)">2015</div>
  <div class="tl-year" style="left:115px;top:149px;color:var(--green)">2016</div>
  <div class="tl-year" style="left:194px;top:87px;color:#ddd">2017</div>
  <div class="tl-year" style="left:274px;top:149px;color:#ddd">2018</div>
  <div class="tl-year" style="left:353px;top:87px;color:var(--blue)">2019</div>
  <div class="tl-cap" style="left:97px;top:59px">Add Text<br>Build a clean slide deck that is simply designed.</div>
  <div class="tl-cap" style="left:256px;top:59px">Add Text<br>Build a clean slide deck that is simply designed.</div>
  <div class="tl-cap" style="left:17px;top:157px">Add Text<br>Build a clean slide deck that is simply designed.</div>
  <div class="tl-cap" style="left:176px;top:157px">Add Text<br>Build a clean slide deck that is simply designed.</div>
  <div class="tl-cap" style="left:322px;top:157px">Add Text<br>Build a clean slide deck that is simply designed.</div>
</section>

<!-- Vertical timeline -->
<section class="slide" style="left:402px;top:460px;width:392px;height:450px">
  <div class="bar bar-green" style="left:0;top:2px;width:392px;height:40px"><span class="title" style="font-size:19px">CLICK TO ADD TITLE</span></div>
  <svg class="abs" style="left:0;top:0" width="392" height="450" viewBox="0 0 392 450">
    <line x1="84" y1="60" x2="84" y2="401" stroke="var(--blue)" stroke-width="2"/>
    <g fill="var(--blue)">
      <circle cx="84" cy="60" r="3"/><circle cx="84" cy="115" r="3"/><circle cx="84" cy="170" r="3"/>
      <circle cx="84" cy="243" r="3"/><circle cx="84" cy="296" r="3"/><circle cx="84" cy="349" r="3"/><circle cx="84" cy="401" r="3"/>
    </g>
  </svg>
  <div class="vt-year" style="left:20px;top:52px">2013</div>
  <div class="vt-year" style="left:20px;top:107px">2014</div>
  <div class="vt-year" style="left:20px;top:162px">2015</div>
  <div class="vt-year" style="left:23px;top:235px">2016</div>
  <div class="vt-year" style="left:23px;top:288px">2017</div>
  <div class="vt-year" style="left:23px;top:341px">2018</div>
  <div class="vt-year" style="left:23px;top:393px">2019</div>
  <div class="vt-text" style="left:118px;top:57px">Contents Here<br>Build a clean slide deck that is simply and carefully designed.</div>
  <div class="vt-text" style="left:118px;top:112px">Contents Here<br>Build a clean slide deck that is simply and carefully designed.</div>
  <div class="vt-text" style="left:118px;top:167px">Contents Here<br>Build a clean slide deck that is simply and carefully designed.</div>
  <div class="vt-text" style="left:116px;top:240px">Contents Here<br>Build a clean slide deck that is simply and carefully designed.</div>
  <div class="vt-text" style="left:116px;top:293px">Contents Here<br>Build a clean slide deck that is simply and carefully designed.</div>
  <div class="vt-text" style="left:116px;top:346px">Contents Here<br>Build a clean slide deck that is simply and carefully designed.</div>
  <div class="vt-text" style="left:116px;top:395px">Contents Here<br>Build a clean slide deck that is simply and carefully designed.</div>
  <span class="brand footer-brand" style="bottom:10px">Vantor Bellway</span>
</section>

<!-- Feature list with photo -->
<section class="slide" style="left:794px;top:459px;width:406px;height:220px">
  <div class="photo" role="img" aria-label="Photo of two business people shaking hands" style="left:0;top:0;width:214px;height:220px;clip-path:polygon(0 0,100% 0,88% 100%,0 100%);background:linear-gradient(120deg,#1d2736 0%,#56657a 45%,#c4cbd4 80%,#e9ecf0 100%)"></div>
  <span class="title abs" style="left:216px;top:12px;font-size:16px;color:var(--blue)">CLICK TO ADD TITLE</span>
  <span class="abs" style="left:266px;top:33px;font-size:6px;color:#333">Your Subtitle Here</span>
  <svg class="abs" style="left:0;top:0" width="406" height="220" viewBox="0 0 406 220">
    <circle cx="193" cy="64" r="13" fill="var(--blue)"/>
    <circle cx="180" cy="106" r="13" fill="var(--green)"/>
    <circle cx="170" cy="147" r="13" fill="var(--blue)"/>
    <circle cx="161" cy="190" r="13" fill="var(--green)"/>
  </svg>
  <div class="feature-label" style="left:216px;top:53px"><b>IMPROVE</b>Refers to a good or service being offered by a company ideally a product</div>
  <div class="feature-label" style="left:203px;top:95px"><b style="color:var(--green)">REBRAND</b>Refers to a good or service being offered by a company ideally a product</div>
  <div class="feature-label" style="left:193px;top:137px"><b>SUCCESS</b>Refers to a good or service being offered by a company ideally a product</div>
  <div class="feature-label" style="left:183px;top:179px"><b style="color:var(--green)">SUCCESS</b>Refers to a good or service being offered by a company ideally a product</div>
</section>

<!-- Content with photo -->
<section class="slide" style="left:0;top:686px;width:410px;height:228px">
  <div class="photo" role="img" aria-label="Photo of hands reviewing printed charts beside a laptop" style="left:4px;top:0;width:168px;height:228px;background:linear-gradient(160deg,#5b5f66 0%,#b9bec4 40%,#e6e8eb 70%,#7b8088 100%)"></div>
  <div class="bar bar-green" style="left:172px;top:14px;width:238px;height:43px;padding-left:14px"><span class="title" style="font-size:17px">CLICK TO ADD TITLE</span></div>
  <div class="abs" style="left:198px;top:73px;width:200px;font-size:5.5px;line-height:1.35;color:#222">
    <b style="font-size:6px">Contents Title</b><br>Write a short summary of the main idea here, in one or two brief lines, to guide the reader before the points below.
  </div>
  <svg class="abs" style="left:0;top:0" width="410" height="228" viewBox="0 0 410 228">
    <g fill="none" stroke="var(--blue)" stroke-width="2"><circle cx="220" cy="121" r="9"/><circle cx="220" cy="156" r="9"/><circle cx="220" cy="190" r="9"/></g>
  </svg>
  <div class="abs tiny" style="left:233px;top:114px;color:#222"><b>Contents Title</b><br>Click to add title</div>
  <div class="abs tiny" style="left:233px;top:149px;color:#222"><b>Contents Title</b><br>Click to add title</div>
  <div class="abs tiny" style="left:233px;top:183px;color:#222"><b>Contents Title</b><br>Click to add title</div>
</section>

<!-- Options list -->
<section class="slide" style="left:787px;top:679px;width:413px;height:227px">
  <div class="abs" style="left:0;top:0;width:107px;height:227px;background:var(--blue)"></div>
  <div class="option" style="top:16px"><h4>Option Type</h4><p>Short note on this option goes here, kept to one or two brief lines of plain text for the reader.</p></div>
  <div class="option" style="top:66px"><h4>Option Type</h4><p>Short note on this option goes here, kept to one or two brief lines of plain text for the reader.</p></div>
  <div class="option" style="top:117px"><h4>Option Type</h4><p>Short note on this option goes here, kept to one or two brief lines of plain text for the reader.</p></div>
  <div class="option" style="top:167px"><h4>Option Type</h4><p>Short note on this option goes here, kept to one or two brief lines of plain text for the reader.</p></div>
</section>

<!-- Statistic slide -->
<section class="slide" style="left:0;top:916px;width:405px;height:230px">
  <span class="title abs" style="left:25px;top:24px;font-size:17px;color:var(--blue)">CLICK TO ADD TITLE</span>
  <div class="abs" style="left:3px;top:66px;width:402px;height:96px;background:var(--green)"></div>
  <div class="photo" role="img" aria-label="Photo of smiling colleagues reviewing a document together" style="left:185px;top:14px;width:220px;height:216px;clip-path:polygon(25% 0,100% 0,100% 24%,82% 60%,100% 100%,12% 100%,0 60%);background:linear-gradient(135deg,#cfd6dd 0%,#8e98a5 40%,#3d4654 75%,#c8cdd3 100%)"></div>
  <span class="abs" style="left:37px;top:82px;font-family:'Open Sans',Arial,sans-serif;font-weight:700;font-size:46px;color:#e8e8e8">60 %</span>
</section>

<!-- Highlight slide -->
<section class="slide" style="left:405px;top:911px;width:389px;height:235px">
  <div class="photo" role="img" aria-label="Photo of an open-plan office with laptops on a shared desk" style="inset:0;background:linear-gradient(170deg,#3a4049 0%,#6d747e 40%,#9aa1aa 65%,#4b4f55 100%)"></div>
  <div class="abs" style="left:161px;top:55px;width:216px;height:92px;background:rgba(80,100,170,.55);display:flex;align-items:center;padding-left:36px">
    <span class="title" style="font-size:16px">CLICK TO ADD TITLE</span>
  </div>
  <div class="abs" style="left:43px;top:44px;width:120px;height:120px;border-radius:50%;background:var(--blue);display:flex;align-items:center;justify-content:center">
    <span style="font-family:'Open Sans',Arial,sans-serif;font-weight:700;font-size:44px;color:var(--white);letter-spacing:-1px">50%</span>
  </div>
</section>

<!-- Closing slide -->
<section class="slide" style="left:790px;top:916px;width:410px;height:230px">
  <span class="brand abs" style="left:36px;top:68px;font-size:14px">Vantor Bellway</span>
  <span class="abs" style="left:12px;top:103px;font-family:'Oswald',Impact,sans-serif;font-weight:700;font-size:32px;color:var(--blue);letter-spacing:.5px">THANK YOU</span>
  <svg class="abs" style="left:0;top:0" width="410" height="230" viewBox="0 0 410 230" role="img" aria-label="Slanted photo panels of a handshake, a laptop on a desk and a presenter">
    <defs>
      <linearGradient id="panel" x1="0" y1="0" x2="1" y2="1"><stop offset="0" stop-color="#c7ccd2"/><stop offset="1" stop-color="#5e6670"/></linearGradient>
      <linearGradient id="panelDark" x1="0" y1="0" x2="1" y2="1"><stop offset="0" stop-color="#4a525c"/><stop offset="1" stop-color="#25292f"/></linearGradient>
    </defs>
    <polygon points="185,20 254,20 222,134 164,134" fill="url(#panel)"/>
    <polygon points="310,20 403,20 367,134 282,134" fill="url(#panelDark)"/>
    <polygon points="225,97 308,97 269,208 205,208" fill="url(#panelDark)"/>
  </svg>
</section>

</body>
</html>
```